International Wine Label 202001

Need a wine label designed for several new wines from California being exported to Asia. This label should be focused around an animal theme of the flowing: Tiger, Lion, Horse or Eagle. The label should be adaptable to a product line of wines. For example the label could be used for a Cabernet wine, Merlot, Chardonnay or Pinot. A slight modification to the label design should be incorporated to allow for the different varietals. Front label design only. Can utilize photo image in design.
The label would be around 5.75" x 3.50".

Target Market(s)

25-35 year old wine buyers in the global market

Industry/Entity Type

Retail

Font styles to use
Sans Serif

Requirements
Must have
• Wine name based on design (designer suggest name)
Wine varietals
Vintage date
Additional wording area
Nice to have
• Rectangular label preferred Front label only.

```html
<!DOCTYPE html>
<html lang="en">
<head>
<meta charset="utf-8">
<title>Amber Ridge – Label System</title>
<link href="https://fonts.googleapis.com/css2?family=Michroma&display=swap" rel="stylesheet">
<style>
  :root {
    --ink: #231f20;
    --paper: #ffffff;
    --label-grey: #a7a8ab;
    --band-light: #efeff0;
    --label-stock: #e4e4e4;
    --pinot: #fdb913;
    --cabernet: #ef4123;
    --chardonnay: #c2d843;
    --merlot: #5b8fd6;
    --merlot-bright: #1fb6e0;
    --text-light: #e8e8e8;
    --text-mid: #58595b;
  }
  * { box-sizing: border-box; margin: 0; padding: 0; }
  html, body { width: 1200px; height: 1200px; overflow: hidden; background: var(--paper); }
  body { position: relative; font-family: "Michroma", sans-serif; color: var(--ink); }

  .brand-lockup {
    position: absolute; left: 90px; top: 150px; width: 420px;
    display: flex; flex-direction: column; align-items: center;
  }
  .brand-mark { width: 130px; height: 130px; border-radius: 50%; background: var(--ink); }
  .brand-name { margin-top: 40px; font-size: 38px; letter-spacing: 0.04em; line-height: 1; white-space: nowrap; }

  .label {
    position: absolute; width: 270px; height: 192px; background: var(--label-grey);
    display: flex; flex-direction: column; align-items: center; overflow: hidden;
  }
  .label .mark { margin-top: 32px; width: 56px; height: 56px; border-radius: 50%; background: var(--ink); }
  .label .name { margin-top: 20px; font-size: 16px; letter-spacing: 0.04em; line-height: 1; white-space: nowrap; }
  .label .band {
    position: absolute; left: 0; right: 0; bottom: 0; height: 42px;
    border-top: 4px solid var(--accent);
    display: flex; justify-content: flex-end; align-items: center;
    font-size: 12px; letter-spacing: 0.08em; background: var(--ink); color: var(--text-light);
  }
  .label .band.light { background: var(--band-light); color: var(--text-mid); }
  .label .varietal { padding-right: 5px; }
  .label .vintage { height: 100%; display: flex; align-items: center; padding: 0 6px; border-left: 1px solid var(--accent); }

  .pinot { --accent: var(--pinot); left: 600px; top: 62px; }
  .cabernet { --accent: var(--cabernet); left: 874px; top: 62px; }
  .chardonnay { --accent: var(--chardonnay); left: 600px; top: 278px; }
  .merlot { --accent: var(--merlot); left: 874px; top: 278px; }

  .label.large { width: 460px; height: 300px; top: 640px; background: var(--label-stock); }
  .label.large .mark { margin-top: 50px; width: 96px; height: 96px; }
  .label.large .name { margin-top: 30px; font-size: 26px; }
  .label.large .band { height: 64px; font-size: 19px; border-top-width: 6px; }
  .label.large .vintage { padding: 0 12px; }
  .merlot-bottle { --accent: var(--merlot-bright); left: 135px; }
  .cabernet-bottle { --accent: var(--cabernet); left: 615px; }
</style>
</head>
<body>
  <section class="brand-lockup">
    <div class="brand-mark" role="img" aria-label="Amber Ridge brand mark"></div>
    <div class="brand-name">Amber Ridge</div>
  </section>

  <article class="label pinot">
    <div class="mark" role="img" aria-label="Amber Ridge brand mark"></div>
    <div class="name">Amber Ridge</div>
    <div class="band"><span class="varietal">PINOT NOIR</span><span class="vintage">2018</span></div>
  </article>
  <article class="label cabernet">
    <div class="mark" role="img" aria-label="Amber Ridge brand mark"></div>
    <div class="name">Amber Ridge</div>
    <div class="band"><span class="varietal">CABERNET</span><span class="vintage">2018</span></div>
  </article>
  <article class="label chardonnay">
    <div class="mark" role="img" aria-label="Amber Ridge brand mark"></div>
    <div class="name">Amber Ridge</div>
    <div class="band light"><span class="varietal">CHARDONNAY</span><span class="vintage">2015</span></div>
  </article>
  <article class="label merlot">
    <div class="mark" role="img" aria-label="Amber Ridge brand mark"></div>
    <div class="name">Amber Ridge</div>
    <div class="band light"><span class="varietal">MERLOT</span><span class="vintage">2015</span></div>
  </article>

  <article class="label large merlot-bottle">
    <div class="mark" role="img" aria-label="Amber Ridge brand mark"></div>
    <div class="name">Amber Ridge</div>
    <div class="band light"><span class="varietal">MERLOT</span><span class="vintage">2015</span></div>
  </article>
  <article class="label large cabernet-bottle">
    <div class="mark" role="img" aria-label="Amber Ridge brand mark"></div>
    <div class="name">Amber Ridge</div>
    <div class="band"><span class="varietal">CABERNET</span><span class="vintage">2018</span></div>
  </article>
</body>
</html>
```